Simple HVAC & Electrical Contractor Billboard

Leasing a 12'3" H by 49'3" W billboard. I'd like to use our current logo and add a few words to let people know what we do. Looking for a clean simple look.
Our company name is Harold Quince Mechanical - What we are is Air Conditioning & Electrical Contractors.

Our license numbers are TACLA00052618K & TECL71204 they will need to be visible on the sign somewhere.

I'm not sure how much information I want to see on the sign. I want to keep it clean but some of our contact info is as follows. Office # 682-540-9263 - Webpage hqmbrixel.com. I feel like most people can search the name to find the contact info they need but I'll defer to the designers to come up with the best design.

I have attached a couple different logos we have used I the past.

```html
<!DOCTYPE html>
<html lang="en">
<head>
<meta charset="utf-8">
<title>Harold Quince Mechanical – Billboard</title>
<link href="https://fonts.googleapis.com/css2?family=Montserrat:wght@400;500;600&family=Roboto+Condensed:wght@700&family=Roboto:wght@700&display=swap" rel="stylesheet">
<style>
  :root {
    --red: #e3212b;
    --black: #000000;
    --white: #ffffff;
    --stage-light: #ffffff;
    --stage-dark: #3a3a3c;
    --stage-dark-edge: #1f1f20;
    --photo-light: #eeeae6;
    --photo-mid: #c9c6cc;
    --photo-shade: #a9a7ae;
  }
  * { box-sizing: border-box; margin: 0; padding: 0; }
  html, body { width: 1200px; height: 960px; overflow: hidden; }
  body { position: relative; background: var(--stage-light); font-family: "Montserrat", sans-serif; }

  .stage-dark {
    position: absolute; left: 0; top: 518px; width: 1200px; height: 442px;
    background: radial-gradient(ellipse at 50% 55%, #5a5a5c 0%, var(--stage-dark) 45%, var(--stage-dark-edge) 100%);
  }

  .billboard {
    position: absolute; left: 66px; width: 1069px; height: 266px; overflow: hidden;
  }
  .billboard--dark { top: 126px; background: var(--black); color: var(--white); }
  .billboard--light { top: 610px; background: var(--white); color: var(--black); }

  .brand-mark {
    position: absolute; left: 116px; top: 26px; width: 72px; height: 72px; background: var(--red);
  }
  .brand-name {
    position: absolute; left: 18px; top: 122px; width: 290px;
    font-weight: 600; font-size: 29px; line-height: 1; letter-spacing: -0.3px; white-space: nowrap;
  }
  .brand-tagline {
    position: absolute; left: 19px; top: 152px;
    font-weight: 400; font-size: 12.2px; color: var(--red); white-space: nowrap;
  }
  .licenses {
    position: absolute; left: 22px; top: 184px; white-space: nowrap;
  }
  .licenses__label { font-weight: 500; font-size: 13px; color: var(--red); margin-right: 4px; }
  .licenses__numbers { font-family: "Roboto", sans-serif; font-weight: 700; font-size: 10px; }

  .headline {
    position: absolute; left: 356px; top: 30px; width: 290px;
    font-family: "Roboto Condensed", sans-serif; font-weight: 700; text-transform: uppercase;
    transform: rotate(-5deg); transform-origin: left top;
  }
  .headline__lead { color: var(--red); font-size: 41px; line-height: 1; display: block; }
  .headline__sub { font-size: 27px; line-height: 1.1; display: block; margin-left: 3px; }
  .sectors {
    position: absolute; left: 356px; top: 124px; width: 290px; text-align: center;
    font-family: "Roboto Condensed", sans-serif; font-weight: 700; font-size: 20px; line-height: 1.25;
    transform: rotate(-5deg); transform-origin: center;
  }

  .contact-band {
    position: absolute; left: 0; top: 204px; width: 670px; height: 42px; background: var(--red);
    font-family: "Roboto Condensed", sans-serif; font-weight: 700; color: var(--white); white-space: nowrap;
  }
  .contact-band__office { position: absolute; left: 20px; top: 3px; font-size: 29px; }
  .contact-band__divider { position: absolute; left: 316px; top: 2px; font-size: 36px; font-weight: 400; font-family: "Roboto", sans-serif; }
  .contact-band__web { position: absolute; left: 368px; top: 4px; font-size: 27px; }

  .photo-frame { position: absolute; left: 0; top: 0; width: 1069px; height: 266px; pointer-events: none; }
</style>
</head>
<body>
  <div class="stage-dark"></div>

  <section class="billboard billboard--dark">
    <svg class="photo-frame" viewBox="0 0 1069 266" aria-hidden="false">
      <defs>
        <linearGradient id="photoToneDark" x1="0" y1="0" x2="1" y2="1">
          <stop offset="0" stop-color="var(--photo-light)"/>
          <stop offset="0.55" stop-color="var(--photo-mid)"/>
          <stop offset="1" stop-color="var(--photo-shade)"/>
        </linearGradient>
      </defs>
      <polygon points="657,59 1046,0 1064,266 669,266" fill="var(--red)"/>
      <polygon role="img" aria-label="Photo of a woman stretching happily on a light grey sofa in a cool, bright living room" points="672,70 940,0 1035,0 1052,262 683,266" fill="url(#photoToneDark)"/>
    </svg>
    <div class="brand-mark"></div>
    <div class="brand-name">HAROLD QUINCE</div>
    <div class="brand-tagline">Air Conditioning &amp; Electrical Contractors</div>
    <div class="licenses"><span class="licenses__label">license numbers</span><span class="licenses__numbers">TACLA00052618K &amp; TECL71204</span></div>
    <div class="headline"><span class="headline__lead">Specializing in</span><span class="headline__sub">Service &amp; Installation</span></div>
    <div class="sectors">Servicing Residential,<br>Commercial and Industrial Sectors</div>
    <div class="contact-band">
      <span class="contact-band__office">Office # 682-540-9263</span>
      <span class="contact-band__divider">/</span>
      <span class="contact-band__web">website: hqmbrixel.com</span>
    </div>
  </section>

  <section class="billboard billboard--light">
    <svg class="photo-frame" viewBox="0 0 1069 266">
      <defs>
        <linearGradient id="photoToneLight" x1="0" y1="0" x2="1" y2="1">
          <stop offset="0" stop-color="var(--photo-light)"/>
          <stop offset="0.55" stop-color="var(--photo-mid)"/>
          <stop offset="1" stop-color="var(--photo-shade)"/>
        </linearGradient>
      </defs>
      <polygon points="657,59 1046,0 1064,266 669,266" fill="var(--red)"/>
      <polygon role="img" aria-label="Photo of a woman stretching happily on a light grey sofa in a cool, bright living room" points="672,70 940,0 1035,0 1052,262 683,266" fill="url(#photoToneLight)"/>
    </svg>
    <div class="brand-mark"></div>
    <div class="brand-name">HAROLD QUINCE</div>
    <div class="brand-tagline">Air Conditioning &amp; Electrical Contractors</div>
    <div class="licenses"><span class="licenses__label">license numbers</span><span class="licenses__numbers">TACLA00052618K &amp; TECL71204</span></div>
    <div class="headline"><span class="headline__lead">Specializing in</span><span class="headline__sub">Service &amp; Installation</span></div>
    <div class="sectors">Servicing Residential,<br>Commercial and Industrial Sectors</div>
    <div class="contact-band">
      <span class="contact-band__office">Office # 682-540-9263</span>
      <span class="contact-band__divider">/</span>
      <span class="contact-band__web">website: hqmbrixel.com</span>
    </div>
  </section>
</body>
</html>
```